New wine label design aimed at millennials

We have developed 2 new quality wines - a crisp, cool climate Chardonnay from the Orange region and a spicy Shiraz from the Gundagai wine region.

Each of these wines have been made in a distinctly modern style, with less oak and more elegance than most and come from two relatively new but exciting wine regions.

They are distinctly food friendly as a result.

These are classic varieties, with a modern take from 'undiscovered' regions.

We are seeking to target millennial wine drinkers who are possibly new to wine or are early in their journey into wine.

We are after a contemporary single label design (i.e. - not a font ab back label) to be applied to a 'lean green' burgundy bottle that speaks to the modern take on classic varieties from undiscovered regions.

We have already recieved a umber of good designs based on some possible brand names:

Meridell
Kettle and Compass
The Copper Lamplightar

And now we would like to purse labels focusing just on Kettle and Compass (of course if a bolt of lightening strikes you on the other names, feel free!)

the reference to Kettle and Compass comes from a story attached to one of our existing labels – Beatrice Thornbury. The two Thornbury brothers who founded this Vineyard famously borrowed a Kettle and Compass from a well-established winery family in order for them to roam the local foothills in order to find their ideal vineyard site.

We would like to capture this sense of exploration and discovery in what would form a sub-tier label for this brand.

It would still be targeting very much millennial's and so we want the label to look contemporary and urban, but reflect the sense of exploration and discovery awhile referencing the historical authenticity of the whole overarching brand structure.

I have attached a number of inspirational images that would need to be translated into a more modern visual setting.

obviously use of a horse and a matter in some sort of "branded" image would be a first step and obviously the historical/authentic back story combined with a modern anaesthetic lends itself to plain black-and-white.

However, clever use of a modern colour palette would also be very welcome.
Updates

For further inspiration we have been considering the following phrases and words as possible label namesGallivant - giving a sense of freewheeling adventure and explorationHorse & Mattock - referencing an old story of 2 pioneer vignerons being lent a horse and a mattock to go out and find their ideal vineyard sites, introducing concepts of innovation, discovery and authenticityThe Gentleman Vigneron - referencing a founding winemakers nominal descriptor of himself and bringing a true element of authenticity and quality. Added Monday, July 31, 2017

Project Deadline Extended Reason: I am hoping to give some more information and focus on the desired outcomes.The name of the label will be Kettle and Compass.Please review the prior comments to get the background on this and I will add more information as well.I will try to identify and provide some other design work that aligns with what we are trying to achieve also. Added Friday, August 11, 2017

Target Market(s)

Millennials, skewing female 21-35 years, university educated, employed in white collar or professional industry, urban

Font styles to use
Serif
Sans Serif

Colors

Designer to choose colors to be used in the design.

Requirements
Must have
• Modern, contemporary urban look and feel that stands out on the shelf.
• Must be relevant and attractive to millennials.
• Sense of humour or quirkiness to it.
• We like this label amongst many other
• http://www.pelmarkcellars.com/shopwines/
Nice to have
• We will aim to use recycled/low carbon footprint glass in the packaging (i.e. the lean green bottles) so would also aim to use 100% recycled paper on the label and would like to mention this in the design.

```html
<!DOCTYPE html>
<html lang="en">
<head>
<meta charset="utf-8">
<title>Meridell Chardonnay – Label Range</title>
<link rel="stylesheet" href="https://fonts.googleapis.com/css2?family=Archivo+Black&family=Montserrat:wght@600&family=Open+Sans:wght@400;700&display=swap">
<style>
  :root {
    --page: #ffffff;
    --brand-green: #2f6b3a;
    --accent-red: #d4421e;
    --label-tan: #ecdcaa;
    --label-tan-pattern: #cfc48e;
    --label-black: #2b2b2b;
    --label-white: #ffffff;
    --label-white-pattern: #e1e8e2;
    --label-bottle: #d3e4d8;
    --label-bottle-pattern: #bdd0c1;
    --horse-pink: #f0a2a0;
    --horse-teal: #4fb7c4;
    --horse-cream: #f2e6cf;
  }
  * { box-sizing: border-box; margin: 0; padding: 0; }
  html, body { width: 1200px; height: 848px; overflow: hidden; background: var(--page); }
  .sheet { position: relative; width: 1200px; height: 848px; }

  .bottle-art { position: absolute; inset: 0; }

  .neck-horse {
    position: absolute; left: 158px; top: 96px; width: 72px; height: 120px;
    border-radius: 40% 45% 30% 40%;
    background: linear-gradient(150deg, var(--horse-pink), var(--horse-cream) 45%, var(--horse-teal));
    opacity: .9;
  }

  .label {
    position: absolute;
    width: 17em; height: 25.5em;
    font-size: 16px;
    overflow: hidden;
    background: var(--label-bg);
    box-shadow: 0 1px 3px rgba(0,0,0,.18);
    --pattern-h: 16.9em;
    --tag-top: 13.2em;
    --name-top: 7.24em;
    --variety-top: 22.6em;
    --volume-top: 26.2em;
  }
  .label--tan   { --label-bg: var(--label-tan); --pattern: var(--label-tan-pattern); --volume: var(--brand-green); left: 312px; top: 282px; }
  .label--black { --label-bg: var(--label-black); --pattern: transparent; --volume: var(--accent-red); left: 594px; top: 282px; }
  .label--white {
    --label-bg: var(--label-white); --pattern: var(--label-white-pattern); --volume: var(--brand-green);
    --pattern-h: 17.9em; --tag-top: 14.4em; --name-top: 7.54em; --variety-top: 23.2em; --volume-top: 26.2em;
    left: 876px; top: 282px; border: 1px solid #cfcfcf;
  }
  .label--bottle {
    --label-bg: var(--label-bottle); --pattern: var(--label-bottle-pattern); --volume: #6a7a70;
    --tag-top: 14.7em; --name-top: 7.66em; --variety-top: 23.4em; --volume-top: 26.4em;
    font-size: 10.6px; left: 103px; top: 394px; border: 1px solid #f4f8f5;
  }

  .label__pattern {
    position: absolute; left: 0; right: 0; top: 0; height: var(--pattern-h);
    background: linear-gradient(180deg, var(--pattern), var(--label-bg));
    background: var(--pattern);
  }

  .label__horse {
    position: absolute; left: 2.3em; top: 1em; width: 13.4em; height: 15.4em;
    border-radius: 45% 40% 35% 50%;
    background: linear-gradient(145deg, var(--horse-pink) 10%, var(--horse-cream) 40%, var(--horse-teal) 75%);
  }

  .label__tagline {
    position: absolute; right: 1.9em; top: var(--tag-top);
    text-align: right; color: var(--accent-red);
    font-family: "Open Sans", sans-serif; line-height: 1.25;
  }
  .label__tagline .tag-style { font-size: .85em; font-weight: 400; display: block; }
  .label__tagline .tag-region { font-size: 1em; font-weight: 700; display: block; }

  .label__name {
    position: absolute; left: 0; right: 0; top: var(--name-top);
    text-align: center; color: var(--brand-green);
    font-family: "Archivo Black", sans-serif; font-size: 2.5em; font-weight: 400;
    text-transform: uppercase; line-height: 1;
  }
  .label__variety {
    position: absolute; left: 0; right: 0; top: var(--variety-top);
    text-align: center; color: var(--accent-red);
    font-family: "Montserrat", sans-serif; font-weight: 600;
    font-size: .95em; letter-spacing: .3em; line-height: 1;
  }
  .label__volume {
    position: absolute; left: 0; right: 0; top: var(--volume-top);
    text-align: center; color: var(--volume);
    font-family: "Open Sans", sans-serif; font-size: .9em; letter-spacing: .18em; line-height: 1;
  }
</style>
</head>
<body>
<main class="sheet">

  <svg class="bottle-art" width="1200" height="848" viewBox="0 0 1200 848" aria-hidden="true">
    <defs>
      <linearGradient id="glass" x1="0" x2="1" y1="0" y2="0">
        <stop offset="0" stop-color="#b6d1c1"/>
        <stop offset=".35" stop-color="#d8e9de"/>
        <stop offset="1" stop-color="#bcd5c5"/>
      </linearGradient>
    </defs>
    <path d="M162 220 L222 220 C226 262 286 268 286 330 L286 805 Q286 818 272 818 L112 818 Q98 818 98 805 L98 330 C98 268 158 262 162 220 Z" fill="url(#glass)"/>
    <rect x="152" y="40" width="80" height="182" rx="8" fill="#2e6b35"/>
  </svg>
  <div class="neck-horse" role="img" aria-label="Rearing horse illustration on the capsule"></div>

  <section class="label label--bottle">
    <div class="label__pattern" role="img" aria-label="Art deco line pattern"></div>
    <div class="label__horse" role="img" aria-label="Multicoloured rearing horse illustration"></div>
    <p class="label__tagline"><span class="tag-style">CRISP &amp; COOL</span><span class="tag-region">Orange Region</span></p>
    <h2 class="label__name">Meridell</h2>
    <p class="label__variety">CHARDONNAY</p>
    <p class="label__volume">750ml</p>
  </section>

  <section class="label label--tan">
    <div class="label__pattern" role="img" aria-label="Art deco line pattern"></div>
    <div class="label__horse" role="img" aria-label="Multicoloured rearing horse illustration"></div>
    <p class="label__tagline"><span class="tag-style">CRISP &amp; COOL</span><span class="tag-region">Orange Region</span></p>
    <h2 class="label__name">Meridell</h2>
    <p class="label__variety">CHARDONNAY</p>
    <p class="label__volume">750ml</p>
  </section>

  <section class="label label--black">
    <div class="label__horse" role="img" aria-label="Multicoloured rearing horse illustration"></div>
    <p class="label__tagline"><span class="tag-style">CRISP &amp; COOL</span><span class="tag-region">Orange Region</span></p>
    <h2 class="label__name">Meridell</h2>
    <p class="label__variety">CHARDONNAY</p>
    <p class="label__volume">750ml</p>
  </section>

  <section class="label label--white">
    <div class="label__pattern" role="img" aria-label="Art deco line pattern"></div>
    <div class="label__horse" role="img" aria-label="Multicoloured rearing horse illustration"></div>
    <p class="label__tagline"><span class="tag-style">CRISP &amp; COOL</span><span class="tag-region">Orange Region</span></p>
    <h2 class="label__name">Meridell</h2>
    <p class="label__variety">CHARDONNAY</p>
    <p class="label__volume">750ml</p>
  </section>

</main>
</body>
</html>
```